2 banners brivon brand stories / tools / gastronomy

We need 2 banners each for the brand stories on Brivon.
The banners should have the following formats:
(1464px x 625px and 463px x 625px).
2x banner for the brand plomin
2x banners for the brand KALDUR
The banner should be relatively neutral with the logo. Like the example I uploaded.

Brivon

```html
<!DOCTYPE html>
<html lang="en">
<head>
<meta charset="utf-8">
<title>KALDUR and plomin brand story banners</title>
<link rel="stylesheet" href="https://fonts.googleapis.com/css2?family=Michroma&family=Lexend:wght@500&display=swap">
<style>
  :root {
    --page-bg: #ffffff;
    --slate-dark: #262626;
    --slate-mid: #333333;
    --slate-light: #3a3a3a;
    --steel-top: #c7ccd4;
    --steel-light: #dfe3ea;
    --steel-mid: #c4c8cf;
    --steel-low: #a9adb3;
    --logo-light: #ffffff;
    --logo-dark: #1a1a1a;
  }
  * { margin: 0; padding: 0; box-sizing: border-box; }
  html, body {
    width: 1200px;
    height: 840px;
    overflow: hidden;
    background: var(--page-bg);
  }
  .board {
    position: relative;
    width: 1200px;
    height: 840px;
  }
  .banner {
    position: absolute;
    height: 336px;
    overflow: hidden;
  }
  .banner--wide { left: 73px; width: 784px; }
  .banner--narrow { left: 880px; width: 249px; }
  .banner--top { top: 76px; }
  .banner--bottom { top: 430px; }

  .banner--kaldur {
    background:
      radial-gradient(ellipse at 20% 50%, var(--slate-light) 0%, transparent 60%),
      linear-gradient(100deg, var(--slate-mid) 0%, var(--slate-dark) 55%, var(--slate-mid) 100%);
  }
  .banner--plomin {
    background: linear-gradient(180deg,
      var(--steel-top) 0%,
      var(--steel-light) 22%,
      var(--steel-light) 40%,
      var(--steel-mid) 62%,
      var(--steel-mid) 80%,
      var(--steel-low) 100%);
  }

  .wordmark { position: absolute; white-space: nowrap; }
  .wordmark--kaldur {
    font-family: "Michroma", sans-serif;
    font-weight: 400;
    color: var(--logo-light);
    letter-spacing: 0.04em;
    display: flex;
    align-items: center;
    gap: 7px;
  }
  .wordmark--kaldur .dot {
    display: inline-block;
    border: 2px solid var(--logo-light);
    border-radius: 50%;
  }
  .banner--wide .wordmark--kaldur { left: 18px; top: 18px; font-size: 21px; }
  .banner--wide .wordmark--kaldur .dot { width: 28px; height: 28px; }
  .banner--narrow .wordmark--kaldur {
    left: 50%; top: 21px; transform: translateX(-50%); font-size: 13px; gap: 4px;
  }
  .banner--narrow .wordmark--kaldur .dot { width: 18px; height: 18px; border-width: 1.5px; }

  .wordmark--plomin {
    font-family: "Lexend", sans-serif;
    font-weight: 500;
    color: var(--logo-dark);
    letter-spacing: -0.01em;
    line-height: 1;
  }
  .banner--wide .wordmark--plomin { left: 19px; top: 14px; font-size: 38px; }
  .banner--narrow .wordmark--plomin {
    left: 50%; top: 18px; transform: translateX(-50%); font-size: 26px;
  }
</style>
</head>
<body>
  <main class="board">
    <section class="banner banner--wide banner--top banner--kaldur" role="img" aria-label="Dark textured concrete surface background">
      <div class="wordmark wordmark--kaldur"><span class="dot"></span>KALDUR</div>
    </section>
    <section class="banner banner--narrow banner--top banner--kaldur" role="img" aria-label="Dark textured concrete surface background">
      <div class="wordmark wordmark--kaldur"><span class="dot"></span>KALDUR</div>
    </section>
    <section class="banner banner--wide banner--bottom banner--plomin" role="img" aria-label="Brushed stainless steel surface background">
      <div class="wordmark wordmark--plomin">plomin</div>
    </section>
    <section class="banner banner--narrow banner--bottom banner--plomin" role="img" aria-label="Brushed stainless steel surface background">
      <div class="wordmark wordmark--plomin">plomin</div>
    </section>
  </main>
</body>
</html>
```